Business Card Design for Car Wrapping Business

I want a modern business card design for my CAR WRAP business. Here are my requirements:

1)Card needs carbon fibre or any other similar pattern background (refer to Carbon Fibre image and pattern header image), make sure that it should be light,not highlighted.
2)Front of the Card needs a Ostravelli Image (refer to Ostra image), try to highlight car lights,rims,number plate or any part with catchy colour like orange or any other(which suits best)
3)I found back of the card is very sensible in Carbon Fibre Image (attachment).
4) If you have skills to improve my Logo,then it will highly preferred (refer to LOGO image).

Here is the Matter :
Bluehaven Car Wrap
Name-Harjot Dhillon
0491 563 208
17 Quarrystone Drive,Tarneit,Vic( Address)
Facebook : Bluehaven Wrap
Instagram:Bluehaven Wrap

IF you unique ideas to create a catchy and sensible business then please make it by yourself,don't follow my given instructions.

I can only Reward someone who can show Some Car Love in the business card,as you can see that its for CAR RELATED BUSINESS.

If you have any question then please ASK :)
Thank you for your Interest. Good Luck

```html
<!DOCTYPE html>
<html lang="en">
<head>
<meta charset="utf-8">
<title>Bluehaven Wrap – Business Card</title>
<link rel="stylesheet" href="https://fonts.googleapis.com/css2?family=Lato:wght@300;400;700&display=swap">
<style>
  :root {
    --backdrop: #d9d9d9;
    --card: #141414;
    --card-edge: #1c1c1c;
    --ink: #e6e6e6;
    --ink-soft: #a9a9a9;
    --ink-dim: #8a8a8a;
    --car-light: #c9c9c9;
    --car-dark: #3a3a3a;
  }
  * { box-sizing: border-box; margin: 0; padding: 0; }
  html, body { width: 1200px; height: 929px; overflow: hidden; }
  body {
    background: var(--backdrop);
    font-family: "Lato", sans-serif;
    color: var(--ink);
    position: relative;
  }
  .card {
    position: absolute;
    width: 560px;
    height: 320px;
    border-radius: 22px;
    background: var(--card);
    border: 1px solid var(--card-edge);
    box-shadow: 0 14px 30px rgba(0,0,0,0.28);
    overflow: hidden;
  }
  .card--front { left: 110px; top: 90px; }
  .card--back { left: 530px; top: 500px; }

  /* front */
  .brand-mark {
    position: absolute;
    left: 48px;
    top: 150px;
    display: flex;
    align-items: center;
    gap: 10px;
    font-weight: 400;
    font-size: 20px;
    letter-spacing: 6px;
    color: var(--ink);
    text-transform: uppercase;
  }
  .brand-mark__dot {
    width: 12px; height: 12px; border-radius: 50%;
    background: var(--ink);
  }
  .car-art {
    position: absolute;
    right: 0;
    top: 30px;
    width: 300px;
    height: 190px;
    background: linear-gradient(135deg, var(--car-light) 0%, #7d7d7d 45%, var(--car-dark) 100%);
    border-radius: 40% 0 0 35%;
    opacity: 0.9;
  }

  /* back */
  .back__logo {
    position: absolute;
    right: 48px;
    top: 58px;
    display: flex;
    align-items: center;
    gap: 9px;
    font-size: 16px;
    letter-spacing: 5px;
    text-transform: uppercase;
  }
  .back__logo .brand-mark__dot { width: 10px; height: 10px; }
  .company {
    position: absolute;
    left: 40px;
    top: 128px;
    font-size: 36px;
    font-weight: 400;
    color: var(--ink);
  }
  .person {
    position: absolute;
    left: 42px;
    top: 178px;
  }
  .person__name { font-size: 22px; color: var(--ink-soft); font-weight: 400; }
  .person__role { font-size: 12px; color: var(--ink-dim); margin-top: 1px; }
  .contacts {
    position: absolute;
    left: 42px;
    top: 238px;
    list-style: none;
    font-size: 12px;
    color: var(--ink-soft);
  }
  .contacts li { display: flex; align-items: center; gap: 8px; height: 17px; }
  .contacts svg { width: 11px; height: 11px; fill: var(--ink-soft); }
  .contacts .contacts__circle {
    width: 10px; height: 10px; border-radius: 50%;
    background: var(--ink-soft);
  }
  .address {
    position: absolute;
    right: 40px;
    top: 178px;
    text-align: right;
    font-size: 13px;
    line-height: 17px;
    color: var(--ink-soft);
  }
</style>
</head>
<body>

  <section class="card card--front" aria-label="Card front">
    <div class="brand-mark"><span class="brand-mark__dot"></span>Bluehaven</div>
    <div class="car-art" role="img" aria-label="Silver line illustration of a sports car seen from the front three-quarter angle"></div>
  </section>

  <section class="card card--back" aria-label="Card back">
    <div class="back__logo"><span class="brand-mark__dot"></span>Bluehaven</div>
    <h1 class="company">Bluehaven Wrap</h1>
    <div class="person">
      <p class="person__name">Harjot Dhillon</p>
      <p class="person__role">Director</p>
    </div>
    <ul class="contacts">
      <li>
        <svg viewBox="0 0 24 24" aria-hidden="true"><path d="M6.6 10.8a15 15 0 0 0 6.6 6.6l2.2-2.2c.3-.3.7-.4 1-.2 1.1.4 2.3.6 3.6.6.6 0 1 .4 1 1V20c0 .6-.4 1-1 1A17 17 0 0 1 3 4c0-.6.4-1 1-1h3.5c.6 0 1 .4 1 1 0 1.3.2 2.5.6 3.6.1.3 0 .7-.2 1z"/></svg>
        0491 563 208
      </li>
      <li><span class="contacts__circle"></span>Bluehaven Wrap</li>
      <li><span class="contacts__circle"></span>Bluehaven Wrap</li>
    </ul>
    <p class="address">17 Quarrystone Drive,<br>Tarneit,Vic</p>
  </section>

</body>
</html>
```